Painting and decorating services

A flyer that promotes my services as a high quality painter and decorator. My services are fully flexible and we cater for range of customers from the decoration of small homes through to larger businesses. We have the flexibility to work through the night which suits businesses that cannot afford to shut throughout the day. We guarantee a top quality finish and are proud to promote a loyalty scheme for successful referrals.

We are truly a family business that is proud and confident to offer one of the most reliable and friendly services on offer.

Target Market(s)

Family homes, businesses who want offer of 24/7 services

Industry/Entity Type

Painting

Font styles to use
Serif
Sans Serif

Requirements
Must have
• Promotion of reliability, value, quality, service
• Days rates and price work considered
• Promotion of night work
• Loyalty scheme / incentives offerred for referrals
• Concept that we are an extremely hard working team who work extended hours and offer flexibility to customers
• Some picture examples of high quality paint jobs as examples of my work.
• Contact details. Phone 01593847261 or mobile 0763918427 email: tkbrushandrollerworks@quillmail.example
Nice to have
• Notion of friendliness coming across from the advert.
• Commitment to giving the customer what they want and delivering to the highest specifications requested
Should not have
• Any over exaggerated false promises that would make the reader of the flyer believe it's just another blagging tradesman with false marketing and empty promises.

```html
<!DOCTYPE html>
<html lang="en">
<head>
<meta charset="utf-8">
<title>TK Brush &amp; Roller – Painting and Decorating Flyer</title>
<link href="https://fonts.googleapis.com/css2?family=Montserrat:wght@400;500&family=Oswald:wght@500&family=Signika:ital,wght@0,400;0,600;1,400&display=swap" rel="stylesheet">
<style>
  :root {
    --blue: #4458b0;
    --blue-deep: #33479e;
    --sky: #4fc3ee;
    --ink: #2b45a3;
    --paper: #f3f4f7;
    --grey-text: #5a5d66;
    --stage: #e4e4e4;
    --white: #ffffff;
  }
  * { margin: 0; padding: 0; box-sizing: border-box; }
  html, body { width: 1200px; height: 829px; overflow: hidden; background: var(--stage); }
  .canvas { position: relative; width: 1200px; height: 829px; }
  .flyer {
    position: absolute; top: 61px; width: 496px; height: 705px;
    background: var(--paper); overflow: hidden;
    box-shadow: 0 4px 14px rgba(0,0,0,.25);
    font-family: "Signika", sans-serif;
  }
  .flyer--front { left: 67px; }
  .flyer--back { left: 626px; }
  .flyer svg.art { position: absolute; inset: 0; }
  .brand {
    position: absolute; top: 20px;
    font-family: "Signika", sans-serif; font-weight: 600; font-size: 21px;
    color: var(--white); letter-spacing: .4px;
  }
  .flyer--front .brand { left: 26px; }
  .flyer--back .brand { right: 22px; }
  .tagline {
    position: absolute; top: 24px;
    font-family: "Montserrat", sans-serif; font-weight: 500; font-size: 16.5px;
    color: var(--white); letter-spacing: .6px;
  }
  .flyer--front .tagline { right: 19px; }
  .flyer--back .tagline { left: 26px; }
  .section-title {
    position: absolute; left: 0; top: 349px; width: 265px; height: 46px;
    background: var(--blue); border-radius: 0 22px 22px 0;
    box-shadow: 2px 3px 5px rgba(0,0,0,.18);
    font-family: "Oswald", sans-serif; font-weight: 500; font-size: 20.5px;
    color: var(--white); line-height: 46px; padding-left: 20px; letter-spacing: .2px;
  }
  .ticks { list-style: none; position: absolute; color: var(--ink); }
  .ticks li { position: relative; padding-left: 22px; }
  .ticks li::before {
    content: ""; position: absolute; left: 0; top: 50%; width: 14px; height: 14px;
    margin-top: -7px; border-radius: 50%; background: var(--sky);
  }
  .ticks li::after {
    content: ""; position: absolute; left: 3.5px; top: 50%; width: 4px; height: 4px;
    margin-top: -2.5px; border-top: 2px solid var(--white); border-right: 2px solid var(--white);
    transform: rotate(45deg);
  }
  .ticks--promise { left: 15px; top: 409px; font-size: 15.5px; line-height: 26px; }
  .ticks--services { font-size: 17px; line-height: 29px; top: 408px; }
  .ticks--services li { padding-left: 27px; }
  .ticks--services li::before { width: 15px; height: 15px; margin-top: -7.5px; }
  .ticks--services li::after { left: 4px; }
  .col-a { left: 26px; }
  .col-b { left: 255px; }
  .review { position: absolute; left: 14px; top: 572px; width: 340px; }
  .review__stars { color: #f5b21a; font-size: 10px; letter-spacing: 1px; }
  .review__name { color: var(--grey-text); font-size: 10.5px; margin-left: 6px; }
  .review__text { font-style: italic; color: var(--grey-text); font-size: 10.3px; line-height: 14px; margin-top: 3px; }
  .about { position: absolute; left: 20px; top: 551px; width: 462px; }
  .about__title { font-family: "Signika", sans-serif; font-weight: 600; font-size: 11.4px; color: var(--ink); }
  .about__text { color: var(--grey-text); font-size: 11.6px; line-height: 16.4px; margin-top: 8px; text-align: justify; }
  .contact { position: absolute; left: 0; width: 446px; top: 654px; text-align: center; color: var(--white); }
  .contact__line {
    font-family: "Oswald", sans-serif; font-weight: 500; font-size: 20px; letter-spacing: .2px;
    display: flex; align-items: center; justify-content: center; gap: 6px; padding-left: 40px;
  }
  .contact__line svg { width: 19px; height: 19px; }
  .contact__email { font-family: "Montserrat", sans-serif; font-size: 9.8px; letter-spacing: .6px; margin-top: 3px; padding-left: 40px; }
</style>
</head>
<body>
<main class="canvas">

  <section class="flyer flyer--front">
    <svg class="art" viewBox="0 0 496 705" width="496" height="705">
      <defs>
        <linearGradient id="roomTone" x1="0" y1="0" x2="1" y2="1">
          <stop offset="0" stop-color="#e9ebee"/>
          <stop offset=".55" stop-color="#cfd2d6"/>
          <stop offset="1" stop-color="#5c5f63"/>
        </linearGradient>
        <linearGradient id="roofTone" x1="0" y1="0" x2="0" y2="1">
          <stop offset="0" stop-color="#c9cdd2"/><stop offset="1" stop-color="#3d4045"/>
        </linearGradient>
        <linearGradient id="doorTone" x1="0" y1="0" x2="1" y2="0">
          <stop offset="0" stop-color="#b0553c"/><stop offset=".5" stop-color="#2f3338"/><stop offset="1" stop-color="#b35a40"/>
        </linearGradient>
        <linearGradient id="houseTone" x1="0" y1="0" x2="0" y2="1">
          <stop offset="0" stop-color="#dfe3e6"/><stop offset="1" stop-color="#6f7a6a"/>
        </linearGradient>
        <linearGradient id="vanTone" x1="0" y1="0" x2="0" y2="1">
          <stop offset="0" stop-color="#5a7fd0"/><stop offset="1" stop-color="#2c4c9a"/>
        </linearGradient>
      </defs>
      <g role="img" aria-label="Photo of a freshly decorated white open-plan living room and kitchen">
        <path d="M0 190 Q200 62 496 60 V300 Q380 296 250 302 Q110 306 0 342 Z" fill="url(#roomTone)"/>
      </g>
      <path d="M0 0 H496 V60 Q200 62 0 190 Z" fill="var(--white)"/>
      <path d="M0 0 H496 V57 Q200 59 0 186 Z" fill="var(--sky)"/>
      <path d="M0 0 H496 V51 Q200 53 0 178 Z" fill="var(--blue)"/>
      <path d="M0 342 Q110 306 250 302 Q380 296 496 300 V352 Q380 318 250 318 Q110 320 0 358 Z" fill="var(--white)"/>
      <path d="M0 362 Q110 322 250 320 Q380 318 496 356 V368 Q380 332 250 332 Q110 334 0 372 Z" fill="var(--blue)"/>
      <path d="M0 378 Q110 336 250 334 Q380 334 496 372 V378 Q380 342 250 342 Q110 344 0 384 Z" fill="var(--sky)"/>
      <g stroke="var(--white)" stroke-width="5">
        <circle cx="430" cy="298" r="52" fill="url(#roofTone)" role="img" aria-label="Photo of a repainted roof edge and fascia"/>
        <circle cx="430" cy="398" r="52" fill="url(#doorTone)" role="img" aria-label="Photo of a painted front door in a brick wall"/>
        <circle cx="430" cy="490" r="52" fill="url(#houseTone)" role="img" aria-label="Photo of a freshly painted white house exterior"/>
        <circle cx="430" cy="582" r="52" fill="url(#vanTone)" role="img" aria-label="Photo of the company's blue work van"/>
      </g>
      <path d="M0 645 H496 V650 L452 705 H0 Z" fill="var(--blue)"/>
      <path d="M496 648 Q470 668 452 705 L496 705 Z" fill="#d9dbe0"/>
      <path d="M496 648 Q488 680 452 705 Q478 690 496 678 Z" fill="var(--white)"/>
    </svg>

    <div class="brand">TK Brush &amp; Roller</div>
    <div class="tagline">PAINTING AND DECORATING</div>

    <h2 class="section-title">FAMILY, FRIENDLY SERVICES</h2>
    <ul class="ticks ticks--promise">
      <li>Reliability, Value, Quality, Service</li>
      <li>Days Rates And Price Work Considered</li>
      <li>Flexibility To Work Through The Night</li>
      <li>Loyalty Scheme / Incentives Offered For Referrals</li>
      <li>Hard Working Team Who Work Extended Hours</li>
      <li>Flexibility To Customers</li>
    </ul>

    <div class="review">
      <span class="review__stars">★★★★★</span><span class="review__name">Mara</span>
      <p class="review__text">Tom is an amazing decorator! he painted my kitchen and did a perfect job. getting him back to do my living room and dining room! would highly recommend !</p>
    </div>

    <div class="contact">
      <div class="contact__line">CONTACT US TODAY
        <svg viewBox="0 0 20 20" aria-hidden="true"><circle cx="10" cy="10" r="8.8" fill="none" stroke="#fff" stroke-width="1.6"/><path d="M7 5.5 L8.6 5.3 L9.4 7.8 L8.3 8.7 Q9.2 10.8 11.3 11.8 L12.2 10.7 L14.6 11.5 L14.4 13.1 Q13.6 14.4 11.8 14 Q7.2 12.4 5.9 8 Q5.6 6.3 7 5.5 Z" fill="#fff"/></svg>
        01593847261 | 0763918427</div>
      <div class="contact__email">tkbrushandrollerworks@quillmail.example</div>
    </div>
  </section>

  <section class="flyer flyer--back">
    <svg class="art" viewBox="0 0 496 705" width="496" height="705">
      <defs>
        <linearGradient id="homeTone" x1="0" y1="0" x2="0" y2="1">
          <stop offset="0" stop-color="#6b93d6"/>
          <stop offset=".35" stop-color="#8a6a52"/>
          <stop offset=".7" stop-color="#c8b9a0"/>
          <stop offset="1" stop-color="#6d7a55"/>
        </linearGradient>
        <linearGradient id="wallTone" x1="0" y1="0" x2="1" y2="1">
          <stop offset="0" stop-color="#e3e5ea"/><stop offset="1" stop-color="#a8aab2"/>
        </linearGradient>
      </defs>
      <g role="img" aria-label="Photo of a large detached family house with a freshly painted exterior">
        <path d="M0 60 Q296 62 496 190 V345 Q380 305 250 302 Q110 300 0 330 Z" fill="url(#homeTone)"/>
      </g>
      <path d="M0 0 H496 V190 Q296 62 0 60 Z" fill="var(--white)"/>
      <path d="M0 0 H496 V186 Q296 59 0 57 Z" fill="var(--sky)"/>
      <path d="M0 0 H496 V178 Q296 53 0 51 Z" fill="var(--blue)"/>
      <path d="M0 330 Q110 300 250 302 Q380 305 496 345 V360 Q380 320 250 318 Q110 316 0 350 Z" fill="var(--white)"/>
      <path d="M0 354 Q110 320 250 322 Q380 324 496 368 V380 Q380 334 250 334 Q110 332 0 366 Z" fill="var(--blue)"/>
      <path d="M0 370 Q110 336 250 338 Q380 340 496 384 V390 Q380 346 250 344 Q110 342 0 376 Z" fill="var(--sky)"/>
      <circle cx="424" cy="318" r="59" fill="url(#wallTone)" stroke="var(--white)" stroke-width="5" role="img" aria-label="Photo of a hallway finished with patterned wallpaper"/>
      <path d="M0 645 H496 V650 L452 705 H0 Z" fill="var(--blue)"/>
      <path d="M496 648 Q470 668 452 705 L496 705 Z" fill="#d9dbe0"/>
      <path d="M496 648 Q488 680 452 705 Q478 690 496 678 Z" fill="var(--white)"/>
    </svg>

    <div class="tagline">PAINTING AND DECORATING</div>
    <div class="brand">TK Brush &amp; Roller</div>

    <h2 class="section-title">SERVICES AND PRODUCTS</h2>
    <ul class="ticks ticks--services col-a">
      <li>Exterior Decorating</li>
      <li>Floor Painting</li>
      <li>Wallpapers &amp; Paints</li>
      <li>Commercial Painting</li>
    </ul>
    <ul class="ticks ticks--services col-b">
      <li>Painting Contractors</li>
      <li>Industrial Painting</li>
      <li>Paint Stripping</li>
      <li>Paint</li>
    </ul>

    <div class="about">
      <h3 class="about__title">LOCAL WELL ESTABLISHED PAINTING &amp; DECORATING COMPANY.</h3>
      <p class="about__text">TK Brush &amp; Roller is a well established local decorating company that has built up an enviable reputation over the last 12 years. We pride ourselves on our commitment to provide a professional service at all time, whilst maintaining the highest quality of work.</p>
    </div>

    <div class="contact">
      <div class="contact__line">CONTACT US TODAY
        <svg viewBox="0 0 20 20" aria-hidden="true"><circle cx="10" cy="10" r="8.8" fill="none" stroke="#fff" stroke-width="1.6"/><path d="M7 5.5 L8.6 5.3 L9.4 7.8 L8.3 8.7 Q9.2 10.8 11.3 11.8 L12.2 10.7 L14.6 11.5 L14.4 13.1 Q13.6 14.4 11.8 14 Q7.2 12.4 5.9 8 Q5.6 6.3 7 5.5 Z" fill="#fff"/></svg>
        01593847261 | 0763918427</div>
      <div class="contact__email">tkbrushandrollerworks@quillmail.example</div>
    </div>
  </section>

</main>
</body>
</html>
```